" Empresa multidisciplinar de saúde que integra medicina, educação física, fisioterapia, nutrição e psicologia em serviços para pessoas portadoras de doenças ou lesões crônicas, especialmente idosos. "

```html
<!DOCTYPE html>
<html lang="pt-BR">
<head>
<meta charset="UTF-8">
<title>Vitalis – Papel Timbrado</title>
<link href="https://fonts.googleapis.com/css2?family=Montserrat:wght@400;500;600&display=swap" rel="stylesheet">
<style>
  :root {
    --backdrop: #e9eaec;
    --paper: #ffffff;
    --teal: #1fa38a;
    --green: #1faa74;
    --blue: #2a5db0;
    --ink: #3a3f44;
    --faint: #e7e8ea;
    --signature-area: #dfe3e6;
  }
  * { margin: 0; padding: 0; box-sizing: border-box; }
  html, body { width: 1200px; height: 1200px; overflow: hidden; }
  body {
    background: var(--backdrop);
    font-family: "Montserrat", sans-serif;
    color: var(--ink);
    position: relative;
  }
  .letterhead {
    position: absolute;
    left: 198px; top: 35px;
    width: 804px; height: 1130px;
    background: var(--paper);
    box-shadow: 0 6px 24px rgba(0,0,0,.12);
    overflow: hidden;
  }
  .brand {
    position: absolute; left: 88px; top: 70px;
    display: flex; align-items: center; gap: 10px;
  }
  .brand-dot { width: 14px; height: 14px; border-radius: 50%; background: var(--green); }
  .brand-name {
    font-size: 46px; font-weight: 500; color: var(--blue); letter-spacing: -0.5px; line-height: 1;
  }
  .contact {
    position: absolute; right: 70px; top: 62px;
    list-style: none;
    border-left: 1.5px solid var(--green);
    padding-left: 0;
  }
  .contact li {
    display: flex; align-items: center; gap: 8px;
    font-size: 8.5px; color: var(--green); line-height: 1;
    margin: 0 0 9px -5px;
  }
  .contact li::before {
    content: ""; width: 8px; height: 8px; border-radius: 50%;
    background: var(--green); flex: none;
  }
  .body-text {
    position: absolute; left: 88px; top: 175px; width: 560px;
    font-size: 12.4px; line-height: 1.38; text-align: justify;
  }
  .greeting { margin-bottom: 18px; text-align: left; }
  .body-text p + p { margin-top: 16px; }
  .signature {
    position: absolute; left: 88px; top: 890px;
    width: 150px; height: 56px; border-radius: 4px;
    background: var(--signature-area);
  }
  .watermark {
    position: absolute; right: 60px; top: 830px;
    font-size: 150px; font-weight: 400; color: var(--faint);
    letter-spacing: -2px; line-height: 1;
  }
  .footer-band { position: absolute; left: 0; bottom: 0; width: 804px; height: 34px; }
</style>
</head>
<body>
  <main class="letterhead">
    <header class="brand">
      <span class="brand-dot"></span>
      <span class="brand-name">vitalis</span>
    </header>

    <ul class="contact">
      <li>contato@vitalis.com.br</li>
      <li>+55 11 4000 1234</li>
      <li>+55 11 98000 5678</li>
      <li>Rua das Flores, 210</li>
      <li>São Paulo - SP</li>
      <li>www.vitalis.com.br</li>
    </ul>

    <section class="body-text">
      <p class="greeting">Lorem ipsum dolor sit amet<br>consectetuer adipiscing<br>dolore magna aliquam</p>
      <p>Lorem ipsum dolor sit amet, consectetuer adipiscing elit, sed diam nonummy nibh euismod tincidunt ut laoreet dolore magna aliquam erat volutpat. Ut wisi enim ad minim veniam, quis nostrud exerci tation ullamcorper suscipit lobortis nisl ut aliquip ex ea commodo consequat. Duis autem vel eum iriure dolor in hendrerit in vulputate velit esse molestie consequat, vel illum dolore eu feugiat nulla facilisis at vero eros et accumsan et iusto odio dignissim qui blandit praesent luptatum zzril delenit augue duis dolore te feugait nulla facilisi.</p>
      <p>Lorem ipsum dolor sit amet, cons ectetuer adipiscing elit, sed diam nonummy nibh euismod tincidunt ut laoreet dolore magna aliquam erat volutpat. Ut wisi enim ad minim veniam, quis nostrud exerci tation ullamcorper suscipit lobortis nisl ut aliquip ex ea commodo consequat.</p>
      <p>Lorem ipsum dolor sit amet, cons ectetuer adipiscing elit, sed diam nonummy nibh euismod tincidunt ut laoreet dolore magna aliquam erat volutpat. Ut wisi enim ad minim veniam, quis nostrud exerci tation ullamcorper suscipit lobortis nisl ut aliquip ex ea commodo consequat.</p>
      <p>Lorem ipsum dolor sit amet, consectetuer adipiscing elit, sed diam nonummy nibh euismod tincidunt ut laoreet dolore magna aliquam erat volutpat. Ut wisi enim ad minim veniam, quis nostrud exerci tation ullamcorper suscipit lobortis nisl ut aliquip ex ea commodo consequat. Duis autem vel eum iriure dolor in hendrerit in vulputate velit esse molestie consequat, vel illum dolore eu feugiat nulla facilisis at vero eros et accumsan et iusto odio dignissim qui blandit praesent luptatum zzril delenit augue duis dolore te feugait nulla facilisi.</p>
    </section>

    <div class="watermark" aria-hidden="true">vitalis</div>

    <div class="signature" role="img" aria-label="Assinatura manuscrita do responsável"></div>

    <svg class="footer-band" viewBox="0 0 804 34" preserveAspectRatio="none" aria-hidden="true">
      <rect x="0" y="0" width="804" height="34" fill="var(--blue)"/>
      <polygon points="0,0 600,0 570,34 0,34" fill="var(--green)"/>
    </svg>
  </main>
</body>
</html>
```